Bright Path Attorneys Billboard Design for Personal Injury Law Firm

Need a billboard design that we can use for different versions. 1400px X 400px jpeg or png
I have attached the logo and the attorney for the billboard. Attorney Marla Benning
Here is a link to our current website brightpathlegalgroup.example

HEADLINE: HIT BY A TRUCK?
SUBHEAD: NO FEE. BIG FIGHT.
877-GRANTLY

HEADLINE: ACCIDENT?
SUBHEAD: NO FEE, UNLESS WE WIN!
877-GRANTLY

HEADLINE: BIG TRUCK. BIG CASE.
SUBHEAD: YOU PAY $0 UPFRONT
877-GRANTLY

Target Market(s)

People in Car Accident

Industry/Entity Type

Personal Injury Attorneys

```html
<!DOCTYPE html>
<html lang="en">
<head>
<meta charset="UTF-8">
<title>Bright Path Attorneys — Big Truck Billboard</title>
<link rel="stylesheet" href="https://fonts.googleapis.com/css2?family=Anton&family=Poppins:wght@600;700&display=swap">
<style>
  :root {
    --page-bg: #e9ecef;
    --board-white: #ffffff;
    --ink: #1b1b1b;
    --brand-green: #6cbf4a;
    --brand-grey: #4a4a4a;
    --photo-light: #d9d6d2;
    --photo-mid: #a8a39e;
    --photo-dark: #6f6a66;
  }
  * { margin: 0; padding: 0; box-sizing: border-box; }
  html, body {
    width: 1200px;
    height: 900px;
    overflow: hidden;
    background: var(--page-bg);
  }
  .billboard {
    position: absolute;
    left: 40px;
    top: 290px;
    width: 1120px;
    height: 320px;
    background: var(--board-white);
    overflow: hidden;
    box-shadow: 0 10px 30px rgba(0,0,0,0.12);
  }
  .truck-photo {
    position: absolute;
    top: 0;
    right: 0;
    width: 58%;
    height: 100%;
    background:
      radial-gradient(ellipse 35% 60% at 62% 55%, var(--photo-light) 0%, transparent 70%),
      linear-gradient(160deg, var(--photo-light) 0%, var(--photo-mid) 55%, var(--photo-dark) 100%);
  }
  .photo-fade {
    position: absolute;
    top: 0;
    right: 0;
    width: 58%;
    height: 100%;
    background: linear-gradient(to right, var(--board-white) 0%, var(--board-white) 14%, rgba(255,255,255,0) 50%);
  }
  .message {
    position: absolute;
    left: 40px;
    top: 30px;
    width: 580px;
    display: flex;
    flex-direction: column;
    align-items: center;
  }
  .brand {
    display: flex;
    align-items: center;
    gap: 10px;
    font-family: 'Poppins', sans-serif;
    font-weight: 700;
    font-size: 20px;
    line-height: 1.2;
    color: var(--brand-grey);
    letter-spacing: 0.5px;
    margin-bottom: 12px;
  }
  .brand-dot {
    width: 18px;
    height: 18px;
    border-radius: 50%;
    background: var(--brand-green);
  }
  .headline {
    font-family: 'Anton', sans-serif;
    font-weight: 400;
    font-size: 78px;
    line-height: 1;
    color: var(--ink);
    letter-spacing: 0.5px;
    white-space: nowrap;
  }
  .subhead {
    font-family: 'Poppins', sans-serif;
    font-weight: 700;
    font-size: 40px;
    line-height: 1.1;
    color: var(--brand-green);
    margin-top: 8px;
    white-space: nowrap;
  }
  .call-pill {
    margin-top: 10px;
    background: var(--ink);
    color: var(--board-white);
    font-family: 'Poppins', sans-serif;
    font-weight: 700;
    font-size: 44px;
    line-height: 1;
    padding: 10px 34px 12px;
    border-radius: 40px;
    white-space: nowrap;
  }
</style>
</head>
<body>
  <section class="billboard">
    <div class="truck-photo" role="img" aria-label="Black and white photo of a white semi truck with trailer driving on a highway bridge"></div>
    <div class="photo-fade"></div>
    <div class="message">
      <div class="brand">
        <span class="brand-dot"></span>
        <span class="brand-name">Bright Path Attorneys</span>
      </div>
      <h1 class="headline">BIG TRUCK. BIG CASE</h1>
      <p class="subhead">YOU PAY $0 UPFRONT</p>
      <p class="call-pill">Call: 877-GRANTLY</p>
    </div>
  </section>
</body>
</html>
```